create clean, simple business card template

using the logo created now we need to create a simple, elegant business card design to suit

Industry/Entity Type

Business

Font styles to use
Other font styles liked:
• segoe ui

Requirements
Must have
• Front:
"Name:"
"Title:"
"Mobile:"
"email:"
and the logo

Back:
Logo
Nice to have
• Text in black but other graphics etc to match colours in logo as provided

```html
<!DOCTYPE html>
<html lang="en">
<head>
<meta charset="utf-8">
<title>Kestrel Homes – Business Card</title>
<link href="https://fonts.googleapis.com/css2?family=Open+Sans:wght@400;700&display=swap" rel="stylesheet">
<style>
  :root {
    --bg: #e8e5e0;
    --card: #ffffff;
    --olive: #6e5e3c;
    --brand: #7a6437;
    --charcoal: #2f2d2b;
    --text: #4a4a4a;
    --muted: #8f8f8f;
  }
  * { margin: 0; padding: 0; box-sizing: border-box; }
  html, body {
    width: 1200px; height: 1045px; overflow: hidden;
    background: var(--bg);
    font-family: "Open Sans", "Segoe UI", sans-serif;
  }
  .card {
    position: absolute; left: 258px; width: 698px; height: 400px;
    background: radial-gradient(ellipse at center, #ffffff 55%, #f1f1f1 100%);
    box-shadow: 0 4px 14px rgba(0,0,0,0.25);
    overflow: hidden;
  }
  .card--front { top: 80px; }
  .card--back { top: 521px; }
  .card__band {
    position: absolute; left: 0; bottom: 0; width: 100%; height: 18px; display: flex;
  }
  .card__band-dark { width: 50.6%; background: var(--charcoal); }
  .card__band-olive { flex: 1; background: var(--olive); }
  .brand {
    position: absolute; display: flex; align-items: center; gap: 12px;
    font-weight: 700; white-space: nowrap;
  }
  .brand__dot { width: 18px; height: 18px; border-radius: 50%; }
  .brand--front { left: 40px; top: 78px; font-size: 40px; color: var(--brand); }
  .brand--front .brand__dot { background: var(--brand); }
  .brand--back { left: 0; right: 0; top: 180px; justify-content: center; font-size: 40px; color: var(--muted); }
  .brand--back .brand__dot { background: var(--muted); }
  .person { position: absolute; left: 448px; top: 76px; }
  .person__name { font-size: 20px; font-weight: 700; color: var(--brand); }
  .person__title { font-size: 16px; color: var(--text); margin-top: 2px; }
  .contact {
    position: absolute; left: 40px; top: 246px;
    font-size: 16.5px; line-height: 25.5px; color: var(--text);
  }
  .contact strong { color: var(--brand); font-weight: 700; }
  .contact a { color: var(--brand); text-decoration: none; }
</style>
</head>
<body>
  <section class="card card--front">
    <div class="brand brand--front"><span class="brand__dot"></span>Kestrel Homes</div>
    <div class="person">
      <div class="person__name">Lorem Ipsum Dollar</div>
      <div class="person__title">Managing Director</div>
    </div>
    <div class="contact">
      <div>4820 Harbor Lane # 210</div>
      <div>Fairview, OR 97024</div>
      <div><strong>T:</strong> 55310 482 761,&nbsp; <strong>F:</strong> 55310 482 761</div>
      <div>E: hello@kestrelhomes.com , <a>www.kestrelhomes.com</a></div>
    </div>
    <div class="card__band"><span class="card__band-dark"></span><span class="card__band-olive"></span></div>
  </section>

  <section class="card card--back">
    <div class="brand brand--back"><span class="brand__dot"></span>Kestrel Homes</div>
    <div class="card__band"><span class="card__band-dark"></span><span class="card__band-olive"></span></div>
  </section>
</body>
</html>
```